Cask Annals, a definitive reference book on port

My husband has just finished writing a big book on Vintage Port. We need a hardcover book flap design for this book that is impressively huge. It's taken 10 years to research and write. It's 650 pages, interior is A4, exterior 4mm larger, and weighs nearly 3 kilos. It's a special book for people in the wine and port industry, as well as for someone who loves to drink Vintage Port. It can be a beautiful coffeetable book too.

The book is mainly about port and its declared vintages. It's also about the history of port, who drank it, when, how, where, who bought it, for how much, and the port houses are also described in detail.

The wine expert Tobias Quellmore wrote a book about vintage wine in 2002, and my husband would like to have a similar cover for his book. (A photo attached in files). I've attached other photos to give the designers an idea of the look and feel of the 'port culture', as well as photos of the typeface that my husband will be using for the inside hardcover.

Target Market(s)

Wine and port industry. Wine aficionados.

Industry/Entity Type

Winery

Font styles to use
Sans Serif
Script

Colors
ec1f27
1b1b1b
474747
333333
5c5c5c
faa54b

Requirements
Must have
• Book Cover must have Title: "Cask Annals" and "R. K. P. Holloway" (files attached to show proper typeface). One of the files is a flap jacket book cover that my husband designed himself. We're looking for more design ideas, and that pdf is a close winner to what he wants.
Nice to have
• illustration or painting of port glasses, or grapes, or similar. Dark colors, especially port wine, deep red wine colors. Gold writing, black writing, with red/berry/maroon accents. Luxury, elegance, has a masculine edge, traditional, but not too old-school and boring (like grandpa). Textures that are including with the culture of drinking vintage port are leather, velvet, cigar, wood, marble, winter, fireplaces. This sounds quite heavy, but it also should be simple and clean. I hope this isn't too confusing. Thanks!
Should not have
• Bright colors, playfulness.

```html
<!DOCTYPE html>
<html lang="en">
<head>
<meta charset="utf-8">
<title>Cask Annals — R. K. P. Holloway</title>
<link rel="stylesheet" href="https://fonts.googleapis.com/css2?family=Tinos&display=swap">
<style>
  :root {
    --page: #ffffff;
    --cover-black: #0b0a0a;
    --cover-dark: #1b1b1b;
    --cover-grey: #333333;
    --spine-edge: #474747;
    --glass-light: #d8d2c0;
    --port-deep: #4a0f18;
    --gold: #f3a24c;
  }
  * { margin: 0; padding: 0; box-sizing: border-box; }
  html, body {
    width: 1200px;
    height: 1200px;
    overflow: hidden;
    background: var(--page);
  }
  .canvas {
    position: relative;
    width: 1200px;
    height: 1200px;
  }
  .book {
    position: absolute;
    left: 255px;
    top: 65px;
    width: 700px;
    height: 1070px;
    display: flex;
    font-family: "Tinos", "Times New Roman", serif;
    color: var(--gold);
  }

  /* Spine */
  .spine {
    position: relative;
    width: 60px;
    height: 100%;
    background: linear-gradient(90deg, var(--cover-black) 0%, var(--cover-dark) 60%, var(--spine-edge) 92%, var(--cover-dark) 100%);
    overflow: hidden;
  }
  .spine-text {
    position: absolute;
    left: 0;
    width: 60px;
    writing-mode: vertical-rl;
    display: flex;
    align-items: center;
    font-weight: 400;
    line-height: 60px;
    white-space: nowrap;
  }
  .spine-title {
    top: 45px;
    font-size: 40px;
    text-transform: uppercase;
    letter-spacing: -0.5px;
  }
  .spine-author {
    top: 585px;
    font-size: 32px;
  }

  /* Front cover */
  .front-cover {
    position: relative;
    width: 640px;
    height: 100%;
    background: linear-gradient(155deg, var(--cover-grey) 0%, var(--cover-dark) 25%, var(--cover-black) 50%, var(--cover-black) 100%);
    overflow: hidden;
  }
  .cover-photo {
    position: absolute;
    left: 0;
    top: 200px;
    width: 100%;
    height: 870px;
    background:
      radial-gradient(ellipse 170px 260px at 52% 32%, rgba(216, 210, 192, 0.30) 0%, rgba(216, 210, 192, 0.10) 55%, transparent 100%),
      radial-gradient(ellipse 160px 80px at 52% 52%, rgba(120, 24, 38, 0.85) 0%, var(--port-deep) 55%, transparent 100%),
      radial-gradient(ellipse 380px 90px at 55% 94%, rgba(110, 110, 110, 0.35) 0%, transparent 100%);
  }
  .author {
    position: absolute;
    left: 0;
    right: 0;
    top: 28px;
    text-align: center;
    font-size: 60px;
    font-weight: 400;
    line-height: 1;
    letter-spacing: -0.5px;
  }
  .author-rule {
    position: absolute;
    left: 200px;
    width: 260px;
    top: 110px;
    height: 2px;
    background: var(--gold);
  }
  .title {
    position: absolute;
    left: 0;
    right: 0;
    top: 660px;
    text-align: center;
    font-size: 128px;
    font-weight: 400;
    line-height: 100px;
    letter-spacing: -4px;
    text-transform: uppercase;
  }
  .title span { display: block; }

  .rule {
    position: absolute;
    left: 0;
    width: 100%;
    background: var(--gold);
  }
  .rule-thin { top: 953px; height: 2px; }
  .rule-thick { top: 975px; height: 5px; }
</style>
</head>
<body>
<div class="canvas">
  <div class="book">
    <div class="spine">
      <div class="spine-text spine-title">Cask Annals</div>
      <div class="spine-text spine-author">R. K. P. Holloway</div>
      <div class="rule rule-thin"></div>
      <div class="rule rule-thick"></div>
    </div>
    <div class="front-cover">
      <div class="cover-photo" role="img" aria-label="Photograph of port being poured into a large wine glass against a black background, with droplets on a dark surface"></div>
      <div class="author">R. K. P. Holloway</div>
      <div class="author-rule"></div>
      <h1 class="title"><span>Cask</span><span>Annals</span></h1>
      <div class="rule rule-thin"></div>
      <div class="rule rule-thick"></div>
    </div>
  </div>
</div>
</body>
</html>
```